Policy Manual in Education

I need the attached document to be put in a publishable format, with graphics a professional layout, and something that looks more like a professional report, etc. Use color samples from http://www.brvt-lo.com/ and www.kt7up.com, my company is Kt7up, we were hired to write the report and we also built the BRVT resource center http://www.brvt-lo.com/ .

Education

• Look and feel around NM. http://www.brvt-lo.com/ and www.kt7up.com

```html
<!DOCTYPE html>
<html lang="en">
<head>
<meta charset="utf-8">
<title>NM Policy Manual – Page Spreads</title>
<link href="https://fonts.googleapis.com/css2?family=Montserrat:wght@700;800&family=Carlito:wght@400;700&display=swap" rel="stylesheet">
<style>
:root{
  --navy:#04305f;
  --orange:#f7922a;
  --orange-text:#f0812f;
  --ink:#1d1d1d;
  --quote:#1e3a78;
  --stage:#efefef;
  --page:#ffffff;
  --page-edge:#d9d9d9;
}
*{box-sizing:border-box;margin:0;padding:0}
html,body{width:979px;height:1200px;overflow:hidden;background:#fff}
.canvas{position:relative;width:979px;height:1200px;background:#fff}
.stage{position:absolute;left:63px;top:52px;width:852px;height:1096px;background:var(--stage)}
.page{position:absolute;width:412px;height:534px;background:var(--page);border:1px solid var(--page-edge);overflow:hidden;font-family:Carlito,Calibri,sans-serif;color:var(--ink)}
.p1{left:73px;top:62px}.p2{left:494px;top:62px}
.p3{left:73px;top:607px}.p4{left:494px;top:607px}
.brand{position:absolute;left:26px;top:29px;font-family:Montserrat,sans-serif;font-weight:800;font-size:15px;color:var(--navy);letter-spacing:-.3px}
.brand.small{font-size:11px;top:28px}
.brand::before{content:"";display:inline-block;width:7px;height:7px;background:var(--orange);margin-right:4px;vertical-align:1px}
.brand.small::before{width:5px;height:5px}
.cover-photo{position:absolute;left:5px;top:82px;width:402px;height:197px;background:linear-gradient(160deg,#9a8f7f 0%,#c7b59c 35%,#6f8fb0 70%,#4d5a6b 100%)}
.cover-band{position:absolute;left:5px;top:279px;width:402px;height:51px;background:var(--navy);color:#fff;font-family:Montserrat,sans-serif;font-weight:700;font-size:18.5px;text-align:center;line-height:51px}
.cover-blurb{position:absolute;left:55px;top:397px;width:300px;text-align:center;color:var(--orange);font-size:7.4px;line-height:10.6px}
.copyright{position:absolute;left:0;right:0;top:488px;text-align:center;font-size:6.8px}
.title-shapes{position:absolute;left:0;top:0}
.manual-title{position:absolute;left:53px;top:139px;color:#fff;font-family:Montserrat,sans-serif;font-weight:700;font-size:23px}
.intro-head{position:absolute;left:53px;top:251px;color:#fff;font-family:Montserrat,sans-serif;font-weight:700;font-size:11.5px}
.intro-text{position:absolute;left:53px;top:274px;width:145px;color:#fff;font-weight:700;font-size:7.6px;line-height:9.9px}
.content{position:absolute;left:48px;width:317px;font-size:7.1px;line-height:10.7px;text-align:justify}
.content p{margin-bottom:5px}
.content ul{margin:0 0 5px 24px}
.content li{margin-bottom:1px}
.section-label{font-family:Montserrat,sans-serif;font-weight:700;font-size:15.5px;color:var(--orange);line-height:21px}
.section-title{font-family:Montserrat,sans-serif;font-weight:700;font-size:15.5px;color:var(--navy);line-height:21px;text-align:left}
.sub-head{color:var(--orange-text);font-size:10.8px;line-height:14px;text-align:left;margin:20px 0 15px;padding-left:19px;text-indent:-19px}
.quote{color:var(--quote);margin:22px 27px 30px 20px}
.footer-band{position:absolute;left:5px;top:496px;width:358px;height:22px;background:var(--navy);color:#fff;font-size:7.4px;text-align:right;padding-right:11px;line-height:22px}
.page-num{position:absolute;left:370px;top:496px;line-height:22px;font-size:7.6px}
.footer-block{position:absolute;left:386px;top:496px;width:20px;height:22px;background:var(--navy)}
</style>
</head>
<body>
<div class="canvas">
  <div class="stage"></div>

  <section class="page p1">
    <div class="brand">MESAED</div>
    <div class="cover-photo" role="img" aria-label="Group of smiling high school students with backpacks sitting together outdoors"></div>
    <div class="cover-band">NM Policy Manual</div>
    <p class="cover-blurb">Lorem ipsum dolor sit amet, consectetur adipiscing elit, sed do eiusmod tempor incididunt ut labore et dolore magna aliqua. Ut enim ad minim veniam, quis nostrud exercitation ullamco laboris nisi ut aliquip ex ea commodo consequat.</p>
    <p class="copyright">Copyright © 2018 BRVT-NM</p>
  </section>

  <section class="page p2">
    <div class="brand small">MESAED</div>
    <svg class="title-shapes" width="412" height="534" viewBox="0 0 412 534">
      <polygon points="5,90 377,90 302,222 5,222" fill="var(--navy)"/>
      <polygon points="5,222 268,222 148,430 5,430" fill="var(--orange)"/>
    </svg>
    <h1 class="manual-title">NM Policy Manual</h1>
    <h2 class="intro-head">Introduction</h2>
    <p class="intro-text">Lorem ipsum dolor sit amet, consectetur adipiscing elit, sed do eiusmod tempor incididunt ut labore et dolore magna aliqua. Ut enim ad minim veniam, quis nostrud exercitation ullamco laboris nisi ut aliquip ex ea commodo consequat.</p>
  </section>

  <section class="page p3">
    <div class="brand small">MESAED</div>
    <div class="content" style="top:69px">
      <div class="section-label">Section 1</div>
      <h2 class="section-title">History and Purpose of<br>Early College High Schools</h2>
      <h3 class="sub-head">1.1&nbsp;&nbsp; Pressing Problems in Education Led Educators to Seek Strong Solutions</h3>
      <p>Many of our high schools, particularly in high-poverty areas, are struggling to help our children:</p>
      <ul>
        <li>More than 50% of public school students are from low-income families and/or are students of color.</li>
        <li>And yet, 48% of American high schools don’t offer students rigorous coursework.</li>
      </ul>
      <p>We need to develop innovative programs that prepare all students for success in high school, college, and careers, particularly as projections are that by 2025, 68% of jobs will require postsecondary education and training beyond high school.</p>
      <p>Over the past decade, education, the economy, and workforce readiness have converged to redefine what our students require from schools before high school graduation. Multiple factors led this convergence— traditionally underserved student populations constituting a growing proportion of the US school population, the low number of high-school graduates enrolling in postsecondary education, and projections that more occupations in the future would require education beyond high school.</p>
      <p>The National Workforce Office estimates that through 2024, 11 of the 15 (73%) occupations with the highest projected growth will require education beyond high school, and 6 (40%) will require a credential beyond the high-school diploma .</p>
      <p>In light of projections such as these, we need to direct our children to a college education, particularly our low-income students, those whose families have not attended college in the past, and minorities. All these population groups are dramatically underrepresented in college and in high-skilled jobs in the workplace.</p>
    </div>
    <div class="footer-band">NM Policy Manual</div>
    <span class="page-num">2</span>
    <div class="footer-block"></div>
  </section>

  <section class="page p4">
    <div class="brand small">MESAED</div>
    <div class="content" style="top:72px">
      <p>Other problems emerge as state, district, and local educators begin to develop policies for new educational models such as BRVTs.</p>
      <ul>
        <li>Many students from underserved areas will be the first in their family to attend college. Not having the experience of higher education, parents may be unsure or how to guide their children through the college and career options facing them. Parents themselves may need the support of educators as well.</li>
      </ul>
      <h3 class="sub-head" style="margin:18px 0 6px">1.2&nbsp; History and Purpose of Early College High Schools</h3>
      <p>The Early College High School (BRVT) model began in 2002 with funding from the Lena &amp; Ross Harrow Foundation to improve college readiness and completion rates for students underrepresented in postsecondary education.</p>
      <p class="quote">According to Alan Brightwell, Executive Director of Education for the Harrow Foundation, “It’s no wonder students drop out: They are shuffled through the system with adults who hardly know them…. we need to engage and motivate students by giving them the personalized and rigorous courses they need to make a smooth transition to college or the workplace. Early college high school programs are an effective way to accomplish this.”</p>
      <p>This new model for high schools came about in response to the need to increase high-school graduation rates and equip all students with the skills they need to successfully complete college-level work and meet the needs of today’s workplace. Too many students are being left behind every day, unprepared to study further or secure good jobs in today’s economy. Now, however, we have a good change strategy—BRVTs, which respond to the needs of students who would otherwise be left behind, engaging and motivating them, and setting them on their way “early” to college.</p>
      <p>With the BRVT model, we raise the expectations traditionally underserved and high-risk students have for themselves by offering them access to advanced high-school courses and college courses. Students take a blend of high-school and college courses, simultaneously pursuing a high-school diploma and either an associate’s degree or up to two years’ college credits. The advantage of this approach is that students are exposed to higher education early in their lives.</p>
    </div>
    <div class="footer-band">NM Policy Manual</div>
    <span class="page-num">3</span>
    <div class="footer-block"></div>
  </section>
</div>
</body>
</html>
```